Business Card Design for a technology company

Our current business card is outdated and stale.

We need a new look and one soon.

We're a telematics (GPS tracking) company based in Australia. Our audiences are transport and logistics company.

Target Market(s)

1. Transport and Logistics Companies
2. Food and Beverage Manufacturers
3. Concrete Businesses

Industry/Entity Type

Logistics

Contact Information for Business Card

Halvor Pinet

Font styles to use
Sans Serif

Colors
3276b5
0255a3
85acd3
cfdeed
ffffff

Requirements
Must have
• Logo
• "Premium Suppliers of Real Time Temperature Tracking"
• Contact Name
• Business Title
• Address
• Telephone
• Mobile
• Email
• Website URL
Nice to have
• Visual representation of tracking or maps.
Should not have
• Image of a satellite as currently shown

```html
<!DOCTYPE html>
<html lang="en">
<head>
<meta charset="utf-8">
<title>Halvor Pinet – Business Card</title>
<link rel="stylesheet" href="https://fonts.googleapis.com/css2?family=Roboto:wght@400;500;700&display=swap">
<style>
  :root {
    --brand-blue: #0c56a6;
    --ink: #111111;
    --paper: #ffffff;
    --backdrop: #e4e6ea;
    --stripe-black: #0a0a0a;
  }
  * { box-sizing: border-box; margin: 0; padding: 0; }
  html, body { width: 1200px; height: 900px; overflow: hidden; }
  body {
    background: var(--backdrop);
    font-family: "Roboto", Arial, sans-serif;
    display: flex; flex-direction: column; align-items: center; justify-content: center;
    gap: 40px;
  }
  .card {
    position: relative; width: 700px; height: 400px; overflow: hidden;
    box-shadow: 0 6px 18px rgba(0,0,0,.18);
  }
  /* front */
  .card-front { background: var(--brand-blue); color: var(--paper); }
  .card-front .wordmark {
    position: absolute; left: 150px; top: 120px;
    display: flex; align-items: center; gap: 16px;
    font-size: 66px; font-weight: 700; letter-spacing: -1px;
  }
  .wordmark .dot { width: 22px; height: 22px; border-radius: 50%; background: currentColor; flex: none; }
  .card-front .tagline {
    position: absolute; left: 110px; top: 262px;
    font-size: 21px; font-weight: 400; letter-spacing: .2px; white-space: nowrap;
  }
  /* back */
  .card-back { background: var(--paper); color: var(--ink); }
  .card-back .wordmark {
    position: absolute; left: 48px; top: 88px;
    display: flex; align-items: center; gap: 12px;
    font-size: 50px; font-weight: 700; letter-spacing: -1px; color: var(--brand-blue);
  }
  .card-back .wordmark .dot { width: 16px; height: 16px; }
  .rule { position: absolute; left: 248px; top: 210px; width: 412px; height: 2px; background: var(--brand-blue); }
  .person { position: absolute; left: 48px; top: 194px; }
  .person .name { font-size: 20px; font-weight: 500; color: var(--brand-blue); letter-spacing: .5px; }
  .person .role { font-size: 16px; font-weight: 500; margin-top: 2px; }
  .contact-list { position: absolute; left: 48px; top: 262px; list-style: none; font-size: 15px; line-height: 21px; }
  .contact-list li { display: flex; align-items: center; gap: 7px; }
  .contact-list svg { width: 13px; height: 13px; fill: var(--brand-blue); flex: none; }
  .address {
    position: absolute; right: 46px; top: 222px; text-align: right;
    font-size: 16px; font-weight: 500; line-height: 20px; font-style: normal;
  }
  .bottom-bands { position: absolute; left: 0; top: 0; width: 700px; height: 400px; }
  .website { position: absolute; right: 46px; top: 292px; color: var(--paper); font-size: 14px; }
</style>
</head>
<body>
  <section class="card card-front" aria-label="Card front">
    <div class="wordmark"><span class="dot"></span><span>Halvor Pinet</span></div>
    <p class="tagline">Premium Suppliers of Real Time Temperature Tracking</p>
  </section>

  <section class="card card-back" aria-label="Card back">
    <svg class="bottom-bands" viewBox="0 0 700 400" aria-hidden="true">
      <path d="M700 268 H552 Q516 268 503 298 L492 324 Q480 352 446 352 H0 V400 H700 Z" fill="var(--brand-blue)"/>
      <path d="M0 356 H448 Q488 356 502 324 L514 296 Q510 330 500 352 Q486 378 446 378 H0 Z" fill="var(--stripe-black)"/>
      <path d="M0 378 H446 Q486 378 500 352 L498 362 Q484 386 446 386 H0 Z" fill="var(--paper)"/>
    </svg>
    <div class="wordmark"><span class="dot"></span><span>Halvor Pinet</span></div>
    <div class="rule"></div>
    <div class="person">
      <p class="name">MAREN COLBY</p>
      <p class="role">Managing Member</p>
    </div>
    <ul class="contact-list">
      <li><svg viewBox="0 0 16 16" aria-hidden="true"><path d="M3 1h3l1.5 4-2 1.3a9 9 0 0 0 4.2 4.2L11 8.5l4 1.5v3a2 2 0 0 1-2 2A12 12 0 0 1 1 3a2 2 0 0 1 2-2z"/></svg>(555) 014-7270</li>
      <li><svg viewBox="0 0 16 16" aria-hidden="true"><path d="M4 1h8v4H4zM1 6h14v6h-3v3H4v-3H1zM5 10v3h6v-3z"/></svg>(555) 014-6441</li>
      <li><svg viewBox="0 0 16 16" aria-hidden="true"><path d="M1 3h14v10H1zM2 4.2v.6l6 4 6-4v-.6z"/></svg>info@halvorpinet.com</li>
    </ul>
    <address class="address">4120 Marlow Ridge Rd ste 210<br>Dunmore Falls, NV 89310</address>
    <p class="website">www.halvorpinet.com</p>
  </section>
</body>
</html>
```